Newsletter for customers of the IT company

Our company develops the software.
We need to create a monthly newsletter for our customers. The newsletter is distributed by email. Important points to follow:
1/ Newsletter has to include the logo and link to ProfilNet profile of company - https://www.profilnet.example/company/vorek-software-cz/?viewAsMember=true
2/ Corporate color is RGB #003265, you can use it.
3/ Use the most used fonts (calibri, times, trebuchet, verdana, ubuntu etc.).
4/ We need it in the html in final version.
5/ We would like to highlight the offer of webinars (3-4 per month).
6/ There have to be the space for news from company (2-3 per month) and link to website with news in the version of software.
7/ Space for contact.

```html
<!DOCTYPE html>
<html lang="en">
<head>
<meta charset="utf-8">
<title>Vorek Newsletter – January 2024</title>
<link rel="stylesheet" href="https://fonts.googleapis.com/css2?family=Carlito:wght@400;700&family=Poppins:wght@400;500;600;700&display=swap">
<style>
:root{
  --navy:#003265;
  --navy-deep:#0b2350;
  --navy-night:#0a1f45;
  --blue-soft:#2f5fa0;
  --grey-panel:#efeff0;
  --grey-head:#f3f3f3;
  --text:#2b2b2b;
  --white:#ffffff;
}
*{margin:0;padding:0;box-sizing:border-box}
html,body{width:1200px;height:3733px;overflow:hidden;background:var(--white)}
body{font-family:"Carlito","Calibri",sans-serif;color:var(--text)}
a{color:inherit;text-decoration:none}
.newsletter{position:absolute;left:170px;top:102px;width:862px;background:var(--white);box-shadow:0 10px 40px rgba(0,40,90,.18)}

/* header */
.masthead{position:relative;height:128px;background:var(--white)}
.masthead__phone{position:absolute;left:0;top:47px;width:198px;height:33px;background:var(--navy);color:var(--white);font-weight:700;font-size:20px;display:flex;align-items:center;gap:8px;padding-left:18px}
.masthead__brand{position:absolute;left:50%;top:38px;transform:translateX(-50%);display:flex;align-items:center;gap:12px;color:var(--navy);font-weight:700;font-size:44px;letter-spacing:1px}
.masthead__brand .mark{width:34px;height:34px;border-radius:50%;background:var(--navy)}
.masthead__social{position:absolute;right:0;top:0;width:160px;height:128px;background:var(--grey-head);display:flex;align-items:center;justify-content:center}
.social-square{display:block;width:48px;height:48px;background:var(--navy)}
.masthead__rule{height:14px;background:var(--navy)}

/* hero */
.hero{position:relative;height:246px;background:linear-gradient(120deg,#4a6a98 0%,#3a5a8c 45%,#5b77a0 100%);display:flex;flex-direction:column;align-items:center;justify-content:center;color:var(--white)}
.hero h1{font-size:47px;font-weight:700;letter-spacing:.5px;line-height:1;margin-top:-6px}
.hero p{font-size:19px;font-weight:700;margin-top:10px}

/* intro */
.intro{height:641px;padding:50px 55px 0 56px}
.intro h2{color:var(--navy);font-size:30px;font-weight:700;letter-spacing:.3px}
.intro .lead{color:var(--navy);font-size:23px;font-weight:700;line-height:1.35;margin-top:14px}
.intro .body{font-size:18px;line-height:1.38;margin-top:14px}
.intro__row{display:flex;gap:32px;margin-top:30px}
.intro__photo{flex:0 0 286px;height:288px;background:linear-gradient(135deg,#6b5a44,#3c3a3c 55%,#8a6a48)}
.intro__text p{font-size:18px;line-height:1.36;margin-bottom:24px}

/* webinars */
.webinars{height:543px;background:radial-gradient(ellipse at 80% 60%,#143670 0%,var(--navy-deep) 60%,var(--navy-night) 100%);color:var(--white);padding-top:42px;text-align:center}
.webinars h2{font-size:28px;font-weight:700;margin-top:12px;letter-spacing:.3px}
.webinar-grid{display:grid;grid-template-columns:359px 359px;gap:29px;justify-content:center;margin-top:37px;text-align:left}
.webinar{height:112px;background:var(--navy);padding:22px 0 0 43px}
.webinar__date{display:inline-block;background:var(--white);color:var(--navy);font-size:13px;font-weight:700;padding:1px 10px}
.webinar__title{font-size:17px;font-weight:700;margin-top:5px}
.webinar__host{font-size:12px;font-weight:700;margin-top:2px}
.btn-events{display:inline-flex;align-items:center;gap:26px;margin-top:47px;width:246px;height:37px;justify-content:center;background:var(--white);color:var(--navy);font-size:18px;font-weight:700;border:2px solid var(--navy)}

/* speakers */
.speakers{padding-top:78px;text-align:center}
.speakers__kicker{font-family:"Poppins",sans-serif;color:var(--navy);font-size:18px;font-weight:600}
.speakers h2{font-family:"Poppins",sans-serif;color:var(--navy);font-size:34px;font-weight:600;line-height:1.2;margin-top:2px}
.speaker-row{display:flex;gap:21px;justify-content:center;margin-top:32px;text-align:left}
.speaker{width:237px;height:516px;background:var(--navy);color:var(--white);font-family:"Poppins",sans-serif}
.speaker__photo{margin-left:19px;height:257px;background:linear-gradient(180deg,#d7d7d9,#b9b9bd)}
.speaker__photo--brick{background:linear-gradient(180deg,#a2563f,#7c4434)}
.speaker__info{padding:22px 18px 0 20px}
.speaker__name{font-size:17px;font-weight:600}
.speaker__role{font-size:11px;font-weight:600;margin-top:2px}
.speaker__info hr{border:0;border-top:1px solid rgba(255,255,255,.55);width:160px;margin:12px 0 16px}
.speaker__info p{font-size:13px;line-height:1.18;margin-bottom:14px}

/* news */
.news{padding:30px 0 0 56px}
.news__bar{width:749px;height:41px;background:linear-gradient(90deg,var(--navy) 0%,var(--navy) 60%,#0f3d78 100%);border-radius:2px;color:var(--white);font-size:27px;font-weight:700;padding-left:40px;line-height:41px;letter-spacing:.3px}
.news-item{width:749px;height:206px;background:var(--grey-panel);margin-top:29px;padding:20px 30px 0 42px}
.news-item h3{color:var(--navy);font-size:24px;font-weight:700;letter-spacing:.3px}
.news-item time{display:block;font-size:12px;font-weight:700;margin-top:3px;color:#444}
.news-item p{font-size:15px;line-height:1.38;margin-top:4px}
.news-item a{display:inline-block;color:var(--navy);font-size:15px;text-decoration:underline;margin-top:3px}

/* footer */
.footer-photo{margin-top:74px;height:177px;background:linear-gradient(160deg,#1c3258,#2a4670 50%,#172b4f)}
.footer{display:flex;height:227px}
.footer__contact{flex:1;background:var(--navy-deep);color:var(--white);padding:32px 0 0 56px;position:relative}
.footer__contact h2{font-size:30px;font-weight:700;letter-spacing:.3px}
.contact-row{display:flex;gap:22px;margin-top:20px}
.contact-item{font-size:15px;font-weight:700;line-height:1.25}
.contact-item svg{display:block;margin-bottom:10px}
.copyright{position:absolute;left:56px;bottom:14px;font-size:9px;font-weight:700}
.footer__follow{flex:0 0 246px;background:var(--blue-soft);color:var(--white);text-align:center;padding-top:36px}
.footer__follow p{font-size:31px;font-weight:700;line-height:1.3}
.footer__follow .social-square{margin:22px auto 0;width:49px;height:49px}
</style>
</head>
<body>
<main class="newsletter">
  <header class="masthead">
    <div class="masthead__phone">
      <svg width="18" height="18" viewBox="0 0 24 24" fill="#fff"><path d="M6.6 10.8a15 15 0 0 0 6.6 6.6l2.2-2.2c.3-.3.7-.4 1-.2 1.1.4 2.3.6 3.6.6.6 0 1 .4 1 1V20c0 .6-.4 1-1 1A17 17 0 0 1 3 4c0-.6.4-1 1-1h3.5c.6 0 1 .4 1 1 0 1.3.2 2.5.6 3.6.1.3 0 .7-.2 1z"/></svg>
      420,555,018
    </div>
    <div class="masthead__brand"><span class="mark"></span>VOREK</div>
    <div class="masthead__social">
      <a class="social-square" href="https://www.profilnet.example/company/vorek-software-cz/?viewAsMember=true" aria-label="Vorek on ProfilNet"></a>
    </div>
  </header>
  <div class="masthead__rule"></div>

  <section class="hero" role="img" aria-label="Photo of people working over documents and a laptop, blue tinted">
    <h1>Newsletter</h1>
    <p>January 2024</p>
  </section>

  <section class="intro">
    <h2>This month from Vorek</h2>
    <p class="lead">Neque porro quisquam est, qui dolorem ipsum quia dolor sit amet, consectetur, adipisci velit sed quia.</p>
    <p class="body">Lorem ipsum dolor sit amet, consectetur adipisicing elit, sed do eiusmod tempor incididunt ut labore et dolore magna aliqua. Ut enim ad minim veniam, quis nostrud exercitation ullamco laboris nisi ut aliquip ex ea commodo consequat.</p>
    <div class="intro__row">
      <div class="intro__photo" role="img" aria-label="Photo of a training session in a computer classroom"></div>
      <div class="intro__text">
        <p>Excepteur sint occaecat cupidatat non proident, sunt in culpa qui officia deserunt mollit anim id est laborum.</p>
        <p>Sed ut perspiciatis unde omnis iste natus error sit voluptatem accusantium doloremque laudantium, e ab illo inventore veritatis et quasi architecto beatae vitae dicta sunt explicabo.</p>
        <p>Nemo enim ipsam voluptatem quia voluptas sit aspernatur aut odit aut fugit, sed quia consequuntur magni dolores eos qui ratione</p>
      </div>
    </div>
  </section>

  <section class="webinars">
    <svg width="36" height="36" viewBox="0 0 24 24" fill="none" stroke="#fff" stroke-width="2"><rect x="3" y="5" width="18" height="16" rx="1"/><path d="M3 10h18M8 3v4M16 3v4"/><path d="M7 13h2M11 13h2M15 13h2M7 17h2M11 17h2M15 17h2" stroke-width="2.2"/></svg>
    <h2>Upcoming Webinars</h2>
    <div class="webinar-grid">
      <article class="webinar"><span class="webinar__date">23/02/2024, 9:00 - 11:00</span><p class="webinar__title">KVX5 Wages - special for schools</p><p class="webinar__host">by Ing. Jana Kovářová</p></article>
      <article class="webinar"><span class="webinar__date">23/02/2024, 9:00 - 11:00</span><p class="webinar__title">KVX5 Wages - special for schools</p><p class="webinar__host">by Ing. Jana Kovářová</p></article>
      <article class="webinar"><span class="webinar__date">23/02/2024, 9:00 - 11:00</span><p class="webinar__title">KVX5 Wages - special for schools</p><p class="webinar__host">by Ing. Jana Kovářová</p></article>
      <article class="webinar"><span class="webinar__date">23/02/2024, 9:00 - 11:00</span><p class="webinar__title">KVX5 Wages - special for schools</p><p class="webinar__host">by Ing. Jana Kovářová</p></article>
    </div>
    <a class="btn-events" href="#">View All Events
      <svg width="12" height="14" viewBox="0 0 12 14"><path d="M0 0l12 7-12 7z" fill="#003265"/></svg>
    </a>
  </section>

  <section class="speakers">
    <p class="speakers__kicker">Here are some</p>
    <h2>Recent Speakers</h2>
    <div class="speaker-row">
      <article class="speaker">
        <div class="speaker__photo" role="img" aria-label="Portrait photo of Dorothy Lane"></div>
        <div class="speaker__info"><p class="speaker__name">Dorothy Lane</p><p class="speaker__role">Designation</p><hr>
          <p>Lorem ipsum dolor sit amet consectetur adipiscing elit, sed do eiusmod tempor incididunt ut labore et lore magna aliqua.</p>
          <p>Quis ipsum suspendisse ultrices gravida. Risus commodo viverra maecenas</p></div>
      </article>
      <article class="speaker">
        <div class="speaker__photo" role="img" aria-label="Portrait photo of DeAndre Miles"></div>
        <div class="speaker__info"><p class="speaker__name">DeAndre Miles</p><p class="speaker__role">Designation</p><hr>
          <p>Lorem ipsum dolor sit amet consectetur adipiscing elit, sed do eiusmod tempor incididunt ut labore et lore magna aliqua.</p>
          <p>Quis ipsum suspendisse ultrices gravida. Risus commodo viverra maecenas</p></div>
      </article>
      <article class="speaker">
        <div class="speaker__photo speaker__photo--brick" role="img" aria-label="Portrait photo of Donovan Hale in front of a brick wall"></div>
        <div class="speaker__info"><p class="speaker__name">Donovan Hale</p><p class="speaker__role">Designation</p><hr>
          <p>Lorem ipsum dolor sit amet consectetur adipiscing elit, sed do eiusmod tempor incididunt ut labore et lore magna aliqua.</p>
          <p>Quis ipsum suspendisse ultrices gravida. Risus commodo viverra maecenas</p></div>
      </article>
    </div>
  </section>

  <section class="news">
    <h2 class="news__bar">In The News</h2>
    <article class="news-item"><h3>Automatic logout when the user is inactive</h3><time>27/11/2023</time>
      <p>Requirements for the security of information systems are constantly increasing in proportion to the growth of threats in cyberspace. Next year, the KVX5 information system will become a regulated service under the new cyber security law and will have to meet a number of security requirements defined in the decrees.</p><a href="#">Read More</a></article>
    <article class="news-item"><h3>Automatic logout when the user is inactive</h3><time>27/11/2023</time>
      <p>Requirements for the security of information systems are constantly increasing in proportion to the growth of threats in cyberspace. Next year, the KVX5 information system will become a regulated service under the new cyber security law and will have to meet a number of security requirements defined in the decrees.</p><a href="#">Read More</a></article>
    <article class="news-item"><h3>Automatic logout when the user is inactive</h3><time>27/11/2023</time>
      <p>Requirements for the security of information systems are constantly increasing in proportion to the growth of threats in cyberspace. Next year, the KVX5 information system will become a regulated service under the new cyber security law and will have to meet a number of security requirements defined in the decrees.</p><a href="#">Read More</a></article>
  </section>

  <div class="footer-photo" role="img" aria-label="Photo of hands typing on a laptop keyboard, blue tinted"></div>
  <footer class="footer">
    <div class="footer__contact">
      <h2>For Inquiries Please Contact Us</h2>
      <div class="contact-row">
        <div class="contact-item">
          <svg width="26" height="26" viewBox="0 0 24 24" fill="#fff"><path d="M6.6 10.8a15 15 0 0 0 6.6 6.6l2.2-2.2c.3-.3.7-.4 1-.2 1.1.4 2.3.6 3.6.6.6 0 1 .4 1 1V20c0 .6-.4 1-1 1A17 17 0 0 1 3 4c0-.6.4-1 1-1h3.5c.6 0 1 .4 1 1 0 1.3.2 2.5.6 3.6.1.3 0 .7-.2 1z"/></svg>
          420,555,018</div>
        <div class="contact-item">
          <svg width="28" height="26" viewBox="0 0 24 24" fill="none" stroke="#fff" stroke-width="2"><circle cx="12" cy="12" r="4"/><path d="M16 8v5a3 3 0 0 0 6 0v-1a10 10 0 1 0-4 8"/></svg>
          podpora@vorek.example</div>
        <div class="contact-item">
          <svg width="26" height="26" viewBox="0 0 24 24" fill="none" stroke="#fff" stroke-width="2"><path d="M12 14s5-5 5-8.5a5 5 0 0 0-10 0C7 9 12 14 12 14z"/><circle cx="12" cy="5.5" r="1.8"/><path d="M6 14l-3 8h18l-3-8"/></svg>
          Vorek spol. s r.o. Lipová 112<br>Nové Město 470 09</div>
      </div>
      <p class="copyright">Copyright 2024 Vorek</p>
    </div>
    <div class="footer__follow">
      <p>Follow us<br>on ProfilNet</p>
      <a class="social-square" href="https://www.profilnet.example/company/vorek-software-cz/?viewAsMember=true" aria-label="Vorek on ProfilNet"></a>
    </div>
  </footer>
</main>
</body>
</html>
```